Design logo, business cards and letterhead for my eye surgery (doctor's) practice

I am a young eye surgeon (Ophthalmic Surgeon) and I need business cards and letterhead designed ( I have a business card brief and a stationary brief submitted). A small logo would also be useful, or some shape that is seen on both the cards and the letterhead. I am based in Perth, Western Australia. I do some laser refractive work ie LASIK, but also other aspects of ophthalmology as well. The design should be conservative, professional and classic, but also, (as someone who sees young patients for laser surgery) a little interesting to people who refer to me and to patients who will be given my card. The details on the letterhead should be:
Dr Ned Palliser
MBBS (Hons), MMed, FRANZCO
Ophthalmic Surgeon

27 Waverton Ave, Subiaco
Western Australia 6008
Phone: (08) 9217 4602
Facsimile: (08) 9217 4619
Email: reception@nedpalliser.com.au
Provider No: 618095KW

The information on the cards should be the same, but with out the provider number.
On the back of the card should say-

Next Appointment________
The rooms can be accessed easily via public transport, or please feel free to park behind the premises in the designated parking bays.

Target Market(s)

General practitioners and optometrists who refer to me and patients

Industry/Entity Type

Business

Contact Information for Business Card

See above

Requirements
Nice to have
• I've attached a little photo which I thought may make a cute logo of sorts on the cards and letterhead.

```html
<!DOCTYPE html>
<html lang="en">
<head>
<meta charset="utf-8">
<title>Dr Ned Palliser – Business Card</title>
<link rel="stylesheet" href="https://fonts.googleapis.com/css2?family=Exo+2:wght@400;600;700&family=Questrial&display=swap">
<style>
  :root {
    --bg: #1e1f21;
    --card: #f7f7f7;
    --navy: #0e4a86;
    --blue: #1f74c4;
    --bright: #1a8ad6;
    --deep: #0b3f78;
    --ink: #2b2b2b;
    --rule: #9a9a9a;
    --faint: #d9dadc;
  }
  * { box-sizing: border-box; margin: 0; padding: 0; }
  html, body { width: 1200px; height: 1000px; overflow: hidden; background: var(--bg); }
  .stage { position: relative; width: 1200px; height: 1000px; }
  .card {
    position: absolute; width: 577px; height: 323px;
    background: var(--card); border-radius: 14px; overflow: hidden;
  }
  .card--front { left: 203px; top: 150px; }
  .card--back { left: 421px; top: 549px; }
  .band {
    position: absolute; left: 0; bottom: 0; width: 577px; height: 34px;
    background: linear-gradient(90deg, var(--bright), var(--deep));
  }

  /* front */
  .brand {
    position: absolute; right: 353px; top: 92px;
    display: flex; align-items: center; gap: 8px;
    font-family: "Exo 2", sans-serif; font-weight: 600; font-size: 14px; color: var(--navy);
  }
  .brand__square { width: 22px; height: 22px; background: var(--blue); }
  .identity { position: absolute; left: 266px; top: 70px; font-family: "Exo 2", sans-serif; }
  .identity__name { font-size: 23px; font-weight: 700; color: var(--navy); letter-spacing: 0.3px; line-height: 28px; }
  .identity__role { font-size: 13px; color: var(--ink); line-height: 17px; }
  .address {
    position: absolute; right: 354px; top: 169px; text-align: right; font-style: normal;
    font-family: "Exo 2", sans-serif; font-size: 13px; color: var(--ink); line-height: 16.5px;
  }
  .divider { position: absolute; left: 244px; top: 170px; width: 1px; height: 48px; background: var(--rule); }
  .contact {
    position: absolute; left: 267px; top: 169px;
    font-family: "Exo 2", sans-serif; font-size: 13px; color: var(--ink); line-height: 16.5px;
  }
  .contact__label { font-weight: 700; color: var(--navy); }

  /* back */
  .appointments__title {
    position: absolute; left: 32px; top: 38px;
    font-family: "Exo 2", sans-serif; font-weight: 700; font-size: 19px; color: var(--navy);
  }
  .appointments__list {
    position: absolute; left: 32px; top: 97px; list-style: none;
    font-family: "Questrial", sans-serif; font-size: 13.5px; color: var(--ink);
  }
  .appointments__list li { height: 37px; white-space: pre; }
  .notice {
    position: absolute; left: 32px; top: 216px; width: 438px;
    font-family: "Questrial", sans-serif; font-size: 13.5px; line-height: 17px; color: var(--ink);
  }
  .watermark-name {
    position: absolute; right: 14px; top: 120px;
    display: flex; align-items: center; gap: 8px;
    font-family: "Exo 2", sans-serif; font-weight: 600; font-size: 22px; color: var(--faint);
  }
  .watermark-name__square { width: 30px; height: 30px; background: var(--faint); }
</style>
</head>
<body>
<main class="stage">

  <section class="card card--front" aria-label="Business card front">
    <div class="brand"><span class="brand__square"></span>Palliser Eye</div>
    <div class="identity">
      <h1 class="identity__name">Dr NED PALLISER</h1>
      <p class="identity__role">MBBS (Hons), MMed, FRANZCO</p>
      <p class="identity__role">Ophthalmic Surgeon</p>
    </div>
    <address class="address">
      27 Waverton Ave, Subiaco<br>
      Western Australia 6008<br>
      Provider No: 618095KW
    </address>
    <span class="divider"></span>
    <p class="contact">
      <span class="contact__label">Tel:</span> (08) 9217 4602<br>
      <span class="contact__label">Fax:</span> (08) 9217 4619<br>
      <span class="contact__label">Email:</span> reception@nedpalliser.com.au
    </p>
    <div class="band" role="img" aria-label="Decorative blue band along the card's lower edge"></div>
  </section>

  <section class="card card--back" aria-label="Business card back">
    <h2 class="appointments__title">YOUR APPOINTMENTS</h2>
    <ol class="appointments__list">
      <li>1. ___am/pm ____________________ ___/___/___</li>
      <li>2. ___am/pm ____________________ ___/___/___</li>
      <li>3. ___am/pm ____________________ ___/___/___</li>
    </ol>
    <p class="notice">The rooms can be accessed easily via public transport, or please feel free to park behind the premises in the designated parking bays.</p>
    <div class="watermark-name"><span class="watermark-name__square"></span>Palliser Eye</div>
    <div class="band" role="img" aria-label="Decorative blue band along the card's lower edge"></div>
  </section>

</main>
</body>
</html>
```